Cedarline Joinery eye catching business card

I need an eye catching business card that reflects my traditional, fun, handmade woodcraft shop. I make high end custom furniture and fine woodworking products, a lot of which are rustic, natural looking. We are a small shop but we produce awesome, one of a kind wood products, and our business card should reflect that. Our target audience is young professionals to retired folks who want a quality, local, handmade product. I'd like the Shop Nearby logo somewhere on the card, BUT not overwhelming, the main focus is my Logo, no preference on color whichever looks the best. Visit my website to get a feel for my company. Cedarlinejoinery.com
Target Market(s)
young professionals to retired folks. Any one who wants to furnish their home with quality handcrafted products.
Industry/Entity Type
Business
Contact Information for Business Card
Marlo Finch (555)417-6382
marlo@cedarlinejoinery.com
www.cedarlinejoinery.com
Look and feel

```html
<!DOCTYPE html>
<html lang="en">
<head>
<meta charset="utf-8">
<title>Cedarline Joinery — Business Card</title>
<link rel="stylesheet" href="https://fonts.googleapis.com/css2?family=Oswald:wght@400;600;700&display=swap">
<style>
  :root {
    --stage: #161616;
    --card-white: #f4f4f4;
    --ink-grey: #5a5a5a;
    --ink-dark: #1c1c1c;
    --rule: #6a6a6a;
    --wood-light: #b7793f;
    --wood-mid: #955a28;
    --wood-dark: #6b3c17;
    --carve: #4a2610;
  }
  * { margin: 0; padding: 0; box-sizing: border-box; }
  html, body { width: 1200px; height: 871px; overflow: hidden; }
  body {
    background: var(--stage);
    font-family: "Oswald", sans-serif;
    position: relative;
  }
  .card {
    position: absolute;
    width: 630px;
    height: 360px;
    border-radius: 4px;
    box-shadow: 0 18px 40px rgba(0,0,0,.55);
    overflow: hidden;
  }
  /* Front */
  .card--front {
    left: 90px; top: 70px;
    background: var(--card-white);
    display: flex;
    align-items: center;
    padding: 0 44px;
  }
  .brand {
    width: 300px;
    display: flex;
    flex-direction: column;
    align-items: center;
    color: var(--ink-grey);
  }
  .brand__row { display: flex; align-items: center; gap: 12px; }
  .brand__mark { width: 16px; height: 16px; background: var(--ink-grey); }
  .brand__name {
    font-weight: 700;
    font-size: 40px;
    letter-spacing: 3px;
    text-transform: uppercase;
    line-height: 1.05;
    text-align: center;
  }
  .brand__tagline {
    margin-top: 16px;
    font-size: 10px;
    font-weight: 400;
    letter-spacing: 2px;
    text-transform: uppercase;
  }
  .divider {
    width: 2px; height: 150px;
    background: var(--rule);
    margin: 0 26px 0 16px;
  }
  .contact { color: var(--ink-dark); }
  .contact__name {
    font-weight: 600;
    font-size: 24px;
    letter-spacing: 1px;
    margin-bottom: 8px;
  }
  .contact__line {
    display: flex; align-items: center; gap: 8px;
    font-size: 16px; font-weight: 600; letter-spacing: .5px;
    margin-bottom: 4px;
  }
  .contact__line svg { width: 16px; height: 16px; fill: var(--ink-grey); flex: none; }
  /* Back */
  .card--back {
    left: 480px; top: 450px;
    display: flex; flex-direction: column;
    align-items: center; justify-content: center;
  }
  .wood {
    position: absolute; inset: 0;
    background:
      radial-gradient(ellipse at 50% 30%, rgba(255,220,170,.25), transparent 65%),
      linear-gradient(90deg, var(--wood-mid), var(--wood-light) 40%, var(--wood-mid) 75%, var(--wood-dark));
  }
  .back__name, .back__url {
    position: relative;
    color: var(--carve);
    text-transform: uppercase;
    text-align: center;
  }
  .back__name {
    font-weight: 700;
    font-size: 54px;
    letter-spacing: 6px;
    line-height: 1.05;
  }
  .back__url {
    margin-top: 34px;
    font-weight: 600;
    font-size: 26px;
    letter-spacing: 3px;
  }
</style>
</head>
<body>
  <section class="card card--front">
    <div class="brand">
      <div class="brand__row">
        <span class="brand__mark"></span>
        <span class="brand__name">Cedarline<br>Joinery</span>
      </div>
      <p class="brand__tagline">Handmade in Alder Bay, SC</p>
    </div>
    <div class="divider"></div>
    <div class="contact">
      <p class="contact__name">Marlo Finch</p>
      <p class="contact__line">
        <svg viewBox="0 0 24 24" aria-hidden="true"><path d="M6.6 10.8a15.1 15.1 0 0 0 6.6 6.6l2.2-2.2a1 1 0 0 1 1-.25 11.4 11.4 0 0 0 3.6.57 1 1 0 0 1 1 1V20a1 1 0 0 1-1 1A17 17 0 0 1 3 4a1 1 0 0 1 1-1h3.5a1 1 0 0 1 1 1c0 1.25.2 2.45.57 3.57a1 1 0 0 1-.25 1z"/></svg>
        (555)417-6382
      </p>
      <p class="contact__line">
        <svg viewBox="0 0 24 24" aria-hidden="true"><path d="M2 5h20v14H2z M2 5l10 8 10-8" fill="none" stroke="#5a5a5a" stroke-width="2"/></svg>
        marlo@cedarlinejoinery.com
      </p>
    </div>
  </section>

  <section class="card card--back">
    <div class="wood" role="img" aria-label="Warm honey-toned wood plank surface"></div>
    <p class="back__name">Cedarline<br>Joinery</p>
    <p class="back__url">www.cedarlinejoinery.com</p>
  </section>
</body>
</html>
```